Audio Visual Services Brochure for Direct Mailing

We are looking to design a direct mailing brochure detailing a new product that we are hoping to install in our immediate surrounding areas in London, UK. We are hoping for a half fold design, with a front page, two page centre spread and a rear page.
We have some very specific information that we want in the middle spread and want to tie this in for the front and rear pages.

Front Page Brief;
This page needs to deliver a problem that most modern households have in that they have too many remote controls (TV, DVD/Bluray, AV Reciever, Satellite TV, Lumo Cast, etc. etc.) We have taken a photo of this situation which may need to be improvded on.
We were hoping to design a page that presents this issue with text that backs up the photo along the lines of, "Does this look familiar? Too many remote controls and a complicated television system?". This page needs to grab the customer if they have this issue.

Centre Spread Brief;
This page presents two solutions to the first pages problem, A single room solution all in one remote control and a whole house solution which details how the system can scale to include lighting, multi-room audio distribution, cctv & security integration, HD/4K video distribution offering all of your video sources on all TV's in the property, Door entry, intercoms etc. etc.
This centre page has been taken from the manufacturers brochure and wants to be kept almost as is. We are very happy with this layout already.

Rear Page Brief;
Here we are hoping to provide a next step / contact us type of page with our company details, perhaps providing some company values and definitely pushing that we have been a SW20 local AV systems specialist since 2004.

Our website is at http://www.brightwave-installs.co.uk which unfortunately still has our old company logo on it but this should help with services etc.

Any other questions please don't hesitate to get in contact.

Target Market(s)

Residential End User Homes - Mid to high income earners that can afford a £1K to £3K remote control system.

Industry/Entity Type

Audio

Font styles to use
Sans Serif

Colors

Designer to choose colors to be used in the design.

Requirements
Must have
• A catchy first page that entices the reader to open the brochure to see the middle section. Front page must be an attention grabber

```html
<!DOCTYPE html>
<html lang="en">
<head>
<meta charset="utf-8">
<title>Brightwave Installs – Half-fold Brochure, Outer Pages</title>
<link href="https://fonts.googleapis.com/css2?family=Lato:wght@300;400&family=Michroma&family=Orbitron:wght@700&family=Oswald:wght@300&display=swap" rel="stylesheet">
<style>
  :root{
    --backdrop:#dcdcdc;
    --paper:#ffffff;
    --brand-blue:#0f4a74;
    --deep-blue:#0a3c60;
    --mid-blue:#1d5580;
    --fold-grey:#e4e5e7;
    --strip-grey:#c8c9cb;
    --photo-grey:#66686b;
    --ink:#2a2a2a;
    --ink-grey:#6c6d70;
  }
  *{box-sizing:border-box;margin:0;padding:0}
  html,body{width:1200px;height:1200px;overflow:hidden;background:var(--backdrop)}
  body{position:relative;font-family:"Lato",sans-serif;color:var(--ink)}

  .spread{position:absolute;left:80px;top:232px;width:1040px;height:735px;display:flex;box-shadow:0 10px 30px rgba(0,0,0,.18)}
  .page{position:relative;width:520px;height:735px;background:var(--paper);overflow:hidden}

  /* ---------- rear page ---------- */
  .rear__divider{position:absolute;left:238px;top:0;width:34px;height:450px;background:var(--strip-grey)}
  .rear__blue{position:absolute;left:272px;top:0;width:248px;height:450px;
    background:linear-gradient(160deg,var(--mid-blue) 0%,var(--brand-blue) 45%,var(--deep-blue) 100%)}
  .rear__identity{position:absolute;left:30px;top:82px;width:206px}
  .wordmark{font-family:"Lato",sans-serif;font-weight:300;color:var(--ink);line-height:1}
  .wordmark__main{display:block;font-size:24px;letter-spacing:.14em}
  .wordmark__sub{display:block;font-size:11.5px;letter-spacing:.3em;margin-top:4px}

  .contact{list-style:none;margin-top:18px;font-size:12px;line-height:1.4;white-space:nowrap}
  .contact li{display:flex;align-items:flex-start;gap:6px}
  .contact svg{width:9px;height:9px;margin-top:4px;flex:none;fill:var(--brand-blue)}
  .contact .indent{padding-left:15px}
  .reg{margin-top:5px;padding-left:15px;font-size:12px;line-height:1.35}
  .reg dt{color:var(--brand-blue)}
  .reg dd{margin-bottom:5px}

  .name-mark{font-family:"Orbitron",sans-serif;font-weight:700;color:var(--brand-blue);letter-spacing:.01em}
  .rear__mark{position:absolute;left:46px;top:388px;font-size:19px}

  .rear__photo{position:absolute;left:0;top:450px;width:520px;height:170px;
    background:linear-gradient(160deg,#7a7c7f 0%,var(--photo-grey) 55%,#5a5b5e 100%)}
  .rear__footer{position:absolute;left:0;top:620px;width:520px;height:115px;text-align:center;padding-top:18px}
  .tagline{font-family:"Orbitron",sans-serif;font-weight:700;color:var(--brand-blue);font-size:14px}
  .since{font-family:"Orbitron",sans-serif;font-weight:700;color:var(--ink-grey);font-size:42px;line-height:1.25;letter-spacing:.02em}

  /* ---------- front page ---------- */
  .front__fold{position:absolute;left:0;top:0;width:58px;height:735px;background:var(--fold-grey)}
  .front__mark{position:absolute;left:120px;top:58px;width:330px;text-align:center;font-size:26px}
  .headline{position:absolute;right:40px;top:285px;text-align:right}
  .headline__lead{font-family:"Oswald",sans-serif;font-weight:300;font-size:40px;line-height:1;color:var(--ink)}
  .headline__hook{font-family:"Orbitron",sans-serif;font-weight:700;font-size:24px;color:var(--brand-blue);margin-top:6px;letter-spacing:.04em}
  .front__photo{position:absolute;left:50px;top:385px;width:470px;height:195px;
    background:
      radial-gradient(ellipse 38% 45% at 60% 55%,rgba(40,42,46,.85) 0%,rgba(60,60,62,.55) 55%,rgba(60,60,62,0) 100%),
      radial-gradient(ellipse 22% 30% at 40% 65%,rgba(235,235,232,.8) 0%,rgba(235,235,232,0) 100%),
      linear-gradient(90deg,#8e9a9c 0%,#a9a59e 22%,#c2a690 45%,#b8967c 75%,#8e9094 100%)}
  .front__bar{position:absolute;left:22px;top:335px;width:108px;height:375px;background:rgba(15,74,116,.72)}
  .front__bar-inner{position:absolute;left:48px;top:350px;width:62px;height:215px;background:rgba(255,255,255,.18)}
  .question{position:absolute;right:36px;top:606px;text-align:right}
  .question__small{font-family:"Michroma",sans-serif;font-size:10.5px;color:var(--ink);letter-spacing:.04em}
  .question__big{font-family:"Orbitron",sans-serif;font-weight:700;font-size:23px;color:var(--brand-blue);margin-top:6px}
</style>
</head>
<body>
<main class="spread">

  <section class="page rear">
    <div class="rear__divider"></div>
    <div class="rear__blue" role="img" aria-label="Abstract faceted deep blue background"></div>

    <div class="rear__identity">
      <div class="wordmark"><span class="wordmark__main">BRIGHTWAVE</span><span class="wordmark__sub">INSTALLS</span></div>
      <ul class="contact">
        <li><svg viewBox="0 0 10 10"><path d="M2 0l2 2-1 1.5a6 6 0 0 0 3.5 3.5L8 6l2 2-1.5 2A8 8 0 0 1 0 1.5z"/></svg>0845 300 4417</li>
        <li><svg viewBox="0 0 10 10"><rect x="2" y="0" width="6" height="3"/><rect x="0" y="3.5" width="10" height="4"/><rect x="2" y="7" width="6" height="3"/></svg>0845 300 4418</li>
        <li><svg viewBox="0 0 10 10"><path d="M0 2h10v6H0z"/></svg>sales@brightwave-installs.co.uk</li>
        <li><svg viewBox="0 0 10 10"><circle cx="5" cy="5" r="5"/></svg>www.brightwave-installs.co.uk</li>
        <li><svg viewBox="0 0 10 10"><path d="M5 0a3.5 3.5 0 0 1 3.5 3.5C8.5 6 5 10 5 10S1.5 6 1.5 3.5A3.5 3.5 0 0 1 5 0z"/></svg>18 Meadowbank Road</li>
        <li class="indent">Raynes Park</li>
        <li class="indent">SW20 9QX</li>
      </ul>
      <dl class="reg">
        <dt>Company Registration</dt><dd>No: 0712648</dd>
        <dt>VAT Registration</dt><dd>No: 915 3308 41</dd>
      </dl>
    </div>

    <div class="rear__mark name-mark">Brightwave</div>

    <div class="rear__photo" role="img" aria-label="Photo of several remote controls standing in a holder on a side table, darkened grey"></div>

    <footer class="rear__footer">
      <p class="tagline">SW20 local AV systems specialist</p>
      <p class="since">SINCE 2004</p>
    </footer>
  </section>

  <section class="page front">
    <div class="front__fold"></div>
    <div class="front__mark name-mark">Brightwave</div>

    <div class="headline">
      <p class="headline__lead">Does this look</p>
      <p class="headline__hook">FAMILIAR?</p>
    </div>

    <div class="front__photo" role="img" aria-label="Photo of hands in a knitted jumper holding a bundle of many TV remote controls"></div>
    <div class="front__bar"></div>
    <div class="front__bar-inner"></div>

    <div class="question">
      <p class="question__small">TOO MANY REMOTE CONTROLS AND A</p>
      <p class="question__big">Television system?</p>
    </div>
  </section>

</main>
</body>
</html>
```